Design of Premium Instant Tea Packaging (Tea in 3 seconds)

We need a fully packaging and sachets design for our new premium instant tea (Tea in 3 seconds) collection to our new brand BrimLeaf. The company is based in Norway and are founded by two Norwegian with a passion for tea and with a mission to share our passion in a faster and easier manner.

We would like a design that gives an exclusive, healthy, tasty and warm feeling. The design should communicate instant tea of high quality.

The tea is one of the first premium instant tea on the market and should give the customer a feeling of exclusive innovation, A new tea company is in town. We don't want to be similar to other old granny tea companies and we hate tea bags :P.

About our products. We offer two different Flavours:
Brim Hibiscus and Brim Lemon. The Brim Hibiscus is sweet and red as blood in its color.

We are looking for a universal design where we can change the color and text based on the flavors. So is important that we get the edible design for front and back of the packages and sachets. Each package contains 10 small sachets where the design of the sachets should be a similar design as the packages itself.

I will provide an example picture/template (just a guideline, not obligatory) from the factory and the sachets, but also from our competitors. Is important that both packaging design and sachets design is editable from both sides if we in the future add new flavors or text.

I will also provide a word file with the necessary text on the pack of the packaging and Nutrition Facts for both of the two flavors. Important that the ingredients are a least in both Norwegian (N) and English (GB). The word file also contains the company information, put on the back of the packaging.

Attached pls find two pictures of design template. Maybe you need them when designing. It's the dimension of 10 sachets/box and 0.6g/sachet the factory use. Our logo BrimLeaf should be on the packaging and the sachets. I also provided the logo in editable format.

Brim Instant Lemon:
GB Ingredients : Lemon, black tea
N Ingredienser: Sitron, svart te

Brim Instant Hibiscus:
GB Ingredients: Hibiscus, rose, black tea and stevia extract
N Ingredienser: Hibiscus, rose, svart te og stevia ekstrakt

Experience the new generation of tea! BrimLeaf® is one of the world fist premium instant tea. Made from real fruit and whole tea leaf, you get incredible tea in seconds. Based on patented cold-brewed technology provide you with the essence of tea, without the need for sugar or preservatives. Brim with health, Brim with taste!

Distributed by Korvenet AS®
PO BOX: 4027
Oslo, Mørkedalsgata 5, Norway
Learn more at BrimLeaf.example

Hope your design can help us stand out from the crowd.

With best regards,

Torvald
CEO of Korvenet As

Target Market(s)

The beverages market, or more correctly the tea market.
The product is Premium Instant Tea.

Font styles to use
Serif

Colors

Designer to choose colors to be used in the design.

Requirements
Must have
• The name of the tea flavor in its representative color.
• Brim Instant Lemon
• Premium Black tea (Smaller letters)
• Brim Instant Hibiscus
• Premium Herbal Tea (Smaller letters)
• General facts:
• * 100 % Natural, no additives, artificial flavors or preventative.
• * 0 fat/ 0 Sugar / 0 Calories.
• * In Crystal instead of tea powder or tea bag.
• * It is soluble in 3 seconds with 200 ml to 300 ml hot or cold pure water.
• Looking for a design where we can change the color and text based on the different flavors. So is important that we get the edible design for the and back of the packages and sachets.
• Ingredients in Norwegian (N) and English(GB) and nutrition values in Norwegian and if possible in English. Remember the company information (provided in the packeging.docx) at the back with a link to our website, www.BrimLeaf.example.
• Must show how the product works on the front and the back. Remember instant tea in 3 seconds from sachets. 10 sachets in each pack, should be a part of the front information, see provided examples.
• Important that we can easily change it our self with affinity or other programs, based on new text or flavor. So we need 360-degree design, so we can change the back and the front, based on what our factory can print out.
• Remember that the design should be reused many times, not just for one of those two flavors above. Simple, but yet elegant and upmarket.
• Each package contains 10 small sachets where the design of the sachets should be a similar design as the packages itself. I will provide an example picture/template from the factory and the sachets, but also from our competitors.
• Is important that both packaging design and sachets design is editable from both sides if we in the future add new flavors or text. I will also provide a word file with the necessary text on the pack of the packaging and Nutrition Facts for both of the two flavors. Important that the ingredients are a least in both Norwegian (N) and English (GB). The word file also contains the company information, put on the back of the packaging.
• Brim Lemon:
• GB Ingredients: Lemon, black tea
• N Ingredienser: Sitron, svart te
• Brim Hibiscus:
• GB Ingredients: Hibiscus, rose, black tea and stevia extract
• N Ingredienser: Hibiscus, rose, svart te og stevia ekstrakt
• Text on the back:
• Experience the new generation of tea! BrimLeaf® is one of the world fist premium instant tea. Made from real fruit and whole tea leaf, you get incredible tea in seconds. Based on patented cold-brewed technology provide you with the essence of tea, without the need for sugar or preservatives. Brim with health, Brim with taste!
• Company information:
• Distributed by Korvenet AS®
• PO BOX: 4027
• Oslo, Mørkedalsgata 5, Norway
• Learn more at www.BrimLeaf.example
Nice to have
• Take a look at Bemo Tea, Vardy Tea and Hollet.
• Especially Hollet since they have a clean and high-class design. https://www.holletleaf.example/tea-by-type/indian-breakfast-25-tea-bags?___SID=U.
• Nice with ® on top of the A on BrimLeaf logo.
• Quiro has also nice designs: https://www.quiroleaf.example/us/en/products/hot.html
• Remember the sticking out / eye-catcher". For both of these proposals, I think that if it had some gold elements in the same way that Sundmark coffee has (a little more expensive for flavor) and that the white color of the proposal one is replaced by light black on the sides and either black or gold in the field where the text. In other words, I think that the packaging should be as identical as possible regardless of taste.
• Feedback for Manufacturer: (Just suggestion from her)
• About the packaging, my suggestion is as follows:
• 1) I think color should match "lemon black tea".We'd better choose the color which in coordination with the flavor, for customer's observation conveniently.
• 2) As for the phrase "cold water instant tea", I think it'd better we remark "stir or shake for better dissolving" or similar meanings in the package. Or describing it by pattern as the attachment FYI. Because these two flavors contain black tea which has enzyme. The molecule of enzyme is a little bigger, so it's a little hard to be totally dissolved by cold water without stirring or shaking.
• Pure tea in hot or cold pure water for you anytime, everywhere on the go (On the back
Should not have
• We hate Parvel, Ashcombe's design. Remember simple, modern and elegant. We are the future of tea, don't make your grandma happy with the design!
• Please avoid using teacups in the design!
• Best regards,
• Torvald

```html
<!DOCTYPE html>
<html lang="en">
<head>
<meta charset="utf-8">
<title>BrimLeaf Instant Lemon – Box Dieline and Sachets</title>
<link rel="stylesheet" href="https://fonts.googleapis.com/css2?family=Cinzel:wght@400;600;700&family=Libre+Baskerville:wght@400;700&display=swap">
<style>
  :root{
    --paper:#ffffff;
    --lime:#c9d51f;
    --lime-deep:#b3bf12;
    --leaf:#8fb23c;
    --leaf-mist:#eef4df;
    --ink:#2a2a2a;
    --dieline:#7fb0d8;
    --dimension:#e0569a;
    --glue:#f4b5d8;
    --tear:#e8584a;
    --hot:#e2601e;
    --cold:#1e73c8;
    --foil-light:#f2f2f2;
    --foil-dark:#bdbdbd;
  }
  html,body{margin:0;padding:0;width:1200px;height:1200px;overflow:hidden;background:var(--paper);}
  .canvas{display:block;width:1200px;height:1200px;}
  .dim-label{font-family:"Libre Baskerville",serif;font-size:13px;fill:var(--dimension);}
  .dim-guide{stroke:var(--dimension);stroke-width:1;stroke-dasharray:2 3;fill:none;}
  .cut-line{stroke:var(--dieline);stroke-width:1.3;fill:var(--paper);}
  .glue-mark{stroke:#555;stroke-width:1;stroke-dasharray:4 3;}
  .tear-strip{stroke:var(--tear);stroke-width:1.1;stroke-dasharray:3 2;fill:none;}
  .glue-band{fill:var(--glue);}
  .flavor-badge{fill:var(--lime);}
  .badge-arc{font-family:"Cinzel",serif;font-weight:700;fill:var(--ink);}
  .badge-name{font-family:"Cinzel",serif;font-weight:700;fill:var(--paper);text-anchor:middle;letter-spacing:.5px;}
  .badge-count{font-family:"Cinzel",serif;font-weight:700;fill:var(--ink);text-anchor:middle;}
  .brand-name{font-family:"Cinzel",serif;font-weight:400;fill:var(--ink);text-anchor:middle;letter-spacing:2px;}
  .brand-dot{fill:none;stroke:var(--leaf);stroke-width:1.2;}
  .logo-plate{fill:var(--paper);}
  .info-plate{fill:var(--paper);}
  .info-flavor{font-family:"Cinzel",serif;font-weight:600;fill:var(--lime-deep);text-anchor:middle;font-size:13px;letter-spacing:.5px;}
  .info-small{font-family:"Libre Baskerville",serif;font-weight:700;fill:var(--ink);font-size:5.2px;}
  .info-body{font-family:"Libre Baskerville",serif;fill:var(--ink);font-size:5px;}
  .info-fact{font-family:"Libre Baskerville",serif;font-weight:700;fill:var(--ink);font-size:4.8px;text-anchor:middle;}
  .info-fact-title{font-family:"Cinzel",serif;font-weight:700;fill:var(--lime-deep);font-size:6.5px;text-anchor:middle;letter-spacing:.5px;}
  .info-center{text-anchor:middle;}
  .howto-hot{font-family:"Libre Baskerville",serif;font-weight:700;fill:var(--hot);font-size:5.5px;}
  .howto-cold{font-family:"Libre Baskerville",serif;font-weight:700;fill:var(--cold);font-size:5.5px;}
  .howto-caption{font-family:"Libre Baskerville",serif;fill:var(--ink);font-size:3.6px;text-anchor:middle;}
  .howto-icon{fill:none;stroke:var(--ink);stroke-width:1.1;stroke-linejoin:round;stroke-linecap:round;}
  .sachet-weight{font-family:"Cinzel",serif;font-weight:700;fill:var(--ink);text-anchor:middle;font-size:14px;}
  .foil{fill:url(#foilSheen);}
</style>
</head>
<body>
<svg class="canvas" viewBox="0 0 1200 1200" xmlns="http://www.w3.org/2000/svg">
  <defs>
    <radialGradient id="leafWashA" cx="45%" cy="40%" r="70%">
      <stop offset="0" stop-color="#cfe0a2"/>
      <stop offset=".45" stop-color="#a9c766" stop-opacity=".75"/>
      <stop offset="1" stop-color="#e9f1d6" stop-opacity=".35"/>
    </radialGradient>
    <radialGradient id="leafWashB" cx="70%" cy="75%" r="55%">
      <stop offset="0" stop-color="#7ea53a" stop-opacity=".55"/>
      <stop offset="1" stop-color="#ffffff" stop-opacity="0"/>
    </radialGradient>
    <linearGradient id="foilSheen" x1="0" y1="0" x2="1" y2="0">
      <stop offset="0" stop-color="var(--foil-dark)"/>
      <stop offset=".5" stop-color="var(--foil-light)"/>
      <stop offset="1" stop-color="var(--foil-dark)"/>
    </linearGradient>
    <path id="arcFront" d="M237,430 A78,78 0 0 1 393,430"/>
    <path id="arcSideA" d="M508,410 A50,50 0 0 1 608,410"/>
    <path id="arcSideB" d="M996,410 A50,50 0 0 1 1096,410"/>
    <path id="arcSachetL" d="M465,990 A45,45 0 0 1 555,990"/>
    <path id="arcSachetC" d="M587,960 A48,48 0 0 1 683,960"/>
    <path id="arcSachetR" d="M715,990 A45,45 0 0 1 805,990"/>
  </defs>

  <!-- ===== Dimension guides ===== -->
  <g class="dimensions">
    <line class="dim-guide" x1="130" y1="50" x2="1105" y2="50"/>
    <line class="dim-guide" x1="130" y1="50" x2="130" y2="797"/>
    <line class="dim-guide" x1="500" y1="50" x2="500" y2="175"/>
    <line class="dim-guide" x1="617" y1="50" x2="617" y2="175"/>
    <line class="dim-guide" x1="988" y1="50" x2="988" y2="175"/>
    <line class="dim-guide" x1="1105" y1="50" x2="1105" y2="175"/>
    <line class="dim-guide" x1="80" y1="60" x2="130" y2="60"/>
    <line class="dim-guide" x1="80" y1="175" x2="130" y2="175"/>
    <line class="dim-guide" x1="80" y1="682" x2="130" y2="682"/>
    <line class="dim-guide" x1="80" y1="797" x2="130" y2="797"/>
    <line class="dim-guide" x1="82" y1="60" x2="82" y2="797"/>
    <text class="dim-label" x="315" y="44" text-anchor="middle">95mm</text>
    <text class="dim-label" x="558" y="44" text-anchor="middle">30mm</text>
    <text class="dim-label" x="802" y="44" text-anchor="middle">95mm</text>
    <text class="dim-label" x="1046" y="44" text-anchor="middle">30mm</text>
    <text class="dim-label" transform="translate(72 118) rotate(-90)" text-anchor="middle">29.5mm</text>
    <text class="dim-label" transform="translate(72 428) rotate(-90)" text-anchor="middle">130mm</text>
    <text class="dim-label" transform="translate(72 740) rotate(-90)" text-anchor="middle">29.5mm</text>
  </g>

  <!-- ===== Flaps ===== -->
  <g class="flaps">
    <path class="cut-line" d="M130,185 L104,200 L104,660 L130,672 Z"/>
    <rect class="glue-band" x="121" y="190" width="9" height="480"/>

    <path class="cut-line" d="M130,175 L130,64 Q130,60 136,60 L494,60 Q500,60 500,66 L500,175"/>
    <path class="cut-line" d="M130,682 L130,793 Q130,797 136,797 L494,797 Q500,797 500,791 L500,682"/>
    <g class="glue-marks">
      <line class="glue-mark" x1="165" y1="140" x2="178" y2="127"/><line class="glue-mark" x1="210" y1="140" x2="223" y2="127"/>
      <line class="glue-mark" x1="255" y1="140" x2="268" y2="127"/><line class="glue-mark" x1="300" y1="140" x2="313" y2="127"/>
      <line class="glue-mark" x1="345" y1="140" x2="358" y2="127"/><line class="glue-mark" x1="390" y1="140" x2="403" y2="127"/>
      <line class="glue-mark" x1="435" y1="140" x2="448" y2="127"/>
      <line class="glue-mark" x1="188" y1="118" x2="201" y2="105"/><line class="glue-mark" x1="233" y1="118" x2="246" y2="105"/>
      <line class="glue-mark" x1="278" y1="118" x2="291" y2="105"/><line class="glue-mark" x1="323" y1="118" x2="336" y2="105"/>
      <line class="glue-mark" x1="368" y1="118" x2="381" y2="105"/><line class="glue-mark" x1="413" y1="118" x2="426" y2="105"/>
      <line class="glue-mark" x1="458" y1="118" x2="471" y2="105"/>
      <line class="glue-mark" x1="165" y1="760" x2="178" y2="747"/><line class="glue-mark" x1="210" y1="760" x2="223" y2="747"/>
      <line class="glue-mark" x1="255" y1="760" x2="268" y2="747"/><line class="glue-mark" x1="300" y1="760" x2="313" y2="747"/>
      <line class="glue-mark" x1="345" y1="760" x2="358" y2="747"/><line class="glue-mark" x1="390" y1="760" x2="403" y2="747"/>
      <line class="glue-mark" x1="435" y1="760" x2="448" y2="747"/>
      <line class="glue-mark" x1="188" y1="738" x2="201" y2="725"/><line class="glue-mark" x1="233" y1="738" x2="246" y2="725"/>
      <line class="glue-mark" x1="278" y1="738" x2="291" y2="725"/><line class="glue-mark" x1="323" y1="738" x2="336" y2="725"/>
      <line class="glue-mark" x1="368" y1="738" x2="381" y2="725"/><line class="glue-mark" x1="413" y1="738" x2="426" y2="725"/>
      <line class="glue-mark" x1="458" y1="738" x2="471" y2="725"/>
    </g>

    <path class="cut-line" d="M502,175 L502,112 Q502,103 512,103 L600,103 Q612,103 612,112 L612,128 L617,134 L617,175"/>
    <path class="cut-line" d="M502,682 L502,785 Q502,794 512,794 L600,794 Q612,794 612,785 L612,730 L617,724 L617,682"/>
    <path class="cut-line" d="M990,175 L990,112 Q990,103 1000,103 L1092,103 Q1103,103 1103,112 L1103,175"/>
    <path class="cut-line" d="M990,682 L990,785 Q990,794 1000,794 L1092,794 Q1103,794 1103,785 L1103,682"/>

    <path class="cut-line" d="M617,175 L617,70 Q617,60 627,60 L978,60 Q988,60 988,70 L988,175"/>
    <path class="tear-strip" d="M625,115 q9,-8 18,0 m8,0 q9,-8 18,0 m8,0 q9,-8 18,0 m8,0 q9,-8 18,0 m8,0 q9,-8 18,0 m8,0 q9,-8 18,0 m8,0 q9,-8 18,0 m8,0 q9,-8 18,0 m8,0 q9,-8 18,0 m8,0 q9,-8 18,0 m8,0 q9,-8 18,0 m8,0 q9,-8 18,0 m8,0 q9,-8 18,0 m8,0 q9,-8 18,0"/>
    <path class="tear-strip" d="M625,140 q9,-8 18,0 m8,0 q9,-8 18,0 m8,0 q9,-8 18,0 m8,0 q9,-8 18,0 m8,0 q9,-8 18,0 m8,0 q9,-8 18,0 m8,0 q9,-8 18,0 m8,0 q9,-8 18,0 m8,0 q9,-8 18,0 m8,0 q9,-8 18,0 m8,0 q9,-8 18,0 m8,0 q9,-8 18,0 m8,0 q9,-8 18,0 m8,0 q9,-8 18,0"/>
    <path class="cut-line" d="M617,682 L617,787 Q617,797 627,797 L978,797 Q988,797 988,787 L988,682"/>
  </g>

  <!-- ===== Box body panels ===== -->
  <g class="box-body">
    <g class="panel-art" role="img" aria-label="Watercolour illustration of green tea leaves and branches covering the box wrap">
      <rect x="130" y="175" width="975" height="507" fill="var(--paper)"/>
      <rect x="130" y="175" width="370" height="507" fill="url(#leafWashA)"/>
      <rect x="130" y="175" width="370" height="507" fill="url(#leafWashB)"/>
      <rect x="500" y="175" width="117" height="507" fill="url(#leafWashA)"/>
      <rect x="617" y="175" width="371" height="507" fill="url(#leafWashA)"/>
      <rect x="617" y="175" width="371" height="507" fill="url(#leafWashB)"/>
      <rect x="988" y="175" width="117" height="507" fill="url(#leafWashA)"/>
    </g>
    <rect class="glue-band" x="1105" y="185" width="8" height="420"/>
    <rect x="130" y="175" width="975" height="507" fill="none" stroke="var(--dieline)" stroke-width=".6" stroke-dasharray="2 3"/>

    <!-- front panel -->
    <g class="front-panel">
      <circle class="flavor-badge" cx="315" cy="430" r="70"/>
      <text class="badge-arc" font-size="13" letter-spacing="1"><textPath href="#arcFront" startOffset="50%" text-anchor="middle">PREMIUM BLACK TEA</textPath></text>
      <text class="badge-name" x="315" y="404" font-size="25">BRIM</text>
      <text class="badge-name" x="315" y="432" font-size="25">INSTANT</text>
      <text class="badge-name" x="315" y="460" font-size="25">LEMON</text>
      <text class="badge-count" x="315" y="479" font-size="12">10 SACHETS</text>
      <text class="badge-count" x="315" y="491" font-size="8">NETT 10x0.6 G</text>
      <rect class="logo-plate" x="205" y="560" width="220" height="122"/>
      <circle class="brand-dot" cx="315" cy="595" r="11"/>
      <text class="brand-name" x="315" y="640" font-size="25">BRIMLEAF</text>
    </g>

    <!-- side panel A -->
    <g class="side-panel">
      <circle class="flavor-badge" cx="558" cy="410" r="44"/>
      <text class="badge-arc" font-size="8.5"><textPath href="#arcSideA" startOffset="50%" text-anchor="middle">PREMIUM BLACK TEA</textPath></text>
      <text class="badge-name" x="558" y="395" font-size="14">BRIM</text>
      <text class="badge-name" x="558" y="413" font-size="14">INSTANT</text>
      <text class="badge-name" x="558" y="431" font-size="14">LEMON</text>
      <text class="badge-count" x="558" y="522" font-size="12">10 SACHETS</text>
      <text class="badge-count" x="558" y="536" font-size="8">NETT 10x0.6 G</text>
      <circle class="brand-dot" cx="558" cy="600" r="7"/>
      <text class="brand-name" x="558" y="625" font-size="11.5" letter-spacing="1">BRIMLEAF</text>
    </g>

    <!-- back panel -->
    <g class="back-panel">
      <rect class="info-plate" x="700" y="190" width="205" height="470"/>
      <circle class="brand-dot" cx="802" cy="215" r="10"/>
      <text class="brand-name" x="802" y="257" font-size="21">BRIMLEAF</text>
      <text class="info-flavor" x="802" y="284">INSTANT LEMON</text>

      <text class="info-small" x="712" y="302">GB INGREDIENTS :</text>
      <text class="info-small" x="712" y="309">LEMON, BLACK TEA</text>
      <text class="info-small" x="810" y="302">DK INGREDIENSER:</text>
      <text class="info-small" x="810" y="309">CITRON, SORT TE</text>
      <text class="info-small" x="712" y="322">N INGREDIENSER:</text>
      <text class="info-small" x="712" y="329">SITRON, SVART TE</text>
      <text class="info-small" x="810" y="322">SE INGREDIENSER:</text>
      <text class="info-small" x="810" y="329">CITRON, SVART TE</text>
      <text class="info-small info-center" x="802" y="344">FIN AINEKSET:</text>
      <text class="info-small info-center" x="802" y="351">SITRUUNA, MUSTA TEE</text>
      <text class="info-small info-center" x="802" y="363">NUTRITION FACTS</text>
      <text class="info-small" x="730" y="372">CAFFEINE</text>
      <text class="info-small" x="820" y="372">2.57G/100G</text>
      <text class="info-small" x="730" y="379">POLYPHENOL</text>
      <text class="info-small" x="820" y="379">13.8G/100G</text>

      <text class="info-body" x="710" y="393">
        <tspan x="710" dy="0">EXPERIENCE THE NEW GENERATION OF TEA! BRIMLEAF®</tspan>
        <tspan x="710" dy="7.5">IS ONE OF THE WORLD FIST PREMIUM INSTANT TEA.</tspan>
        <tspan x="710" dy="7.5">MADE FROM REAL FRUIT AND WHOLE TEA LEAF, YOU GET</tspan>
        <tspan x="710" dy="7.5">INCREDIBLE TEA IN SECONDS. BASED ON PATENTED</tspan>
        <tspan x="710" dy="7.5">COLD-BREWED TECHNOLOGY PROVIDE YOU THE ESSENCE</tspan>
        <tspan x="710" dy="7.5">OF TEA, WITHOUT THE NEED FOR SUGAR OR PRESERVATIVES.</tspan>
        <tspan x="710" dy="7.5">BRIM WITH HEALTH, BRIM WITH TASTE!</tspan>
      </text>

      <text class="howto-hot" x="712" y="465">HOT TEA COOKING</text>
      <text class="howto-cold" x="812" y="465">COLD TEA COOKING</text>
      <g class="howto-icons">
        <rect class="howto-icon" x="708" y="474" width="12" height="18" rx="1"/>
        <line class="howto-icon" x1="708" y1="479" x2="720" y2="479"/>
        <path class="howto-icon" d="M738,474 q5,7 0,10 q-5,-3 0,-10 Z"/>
        <path class="howto-icon" d="M731,486 h16 l-2,8 h-12 Z"/>
        <path class="howto-icon" d="M757,480 h16 l-3,14 h-10 Z"/>
        <rect class="howto-icon" x="816" y="474" width="10" height="16" rx="1"/>
        <line class="howto-icon" x1="816" y1="478" x2="826" y2="478"/>
        <path class="howto-icon" d="M842,475 h6 v4 l3,3 v12 h-12 v-12 l3,-3 Z"/>
        <path class="howto-icon" d="M836,480 l-3,-3 M856,480 l3,-3"/>
        <path class="howto-icon" d="M870,475 h6 v4 l3,3 v12 h-12 v-12 l3,-3 Z"/>
      </g>
      <text class="howto-caption" x="714" y="503"><tspan x="714">Tear</tspan><tspan x="714" dy="4.5">sachet</tspan></text>
      <text class="howto-caption" x="739" y="503"><tspan x="739">Add hot</tspan><tspan x="739" dy="4.5">water</tspan></text>
      <text class="howto-caption" x="765" y="503"><tspan x="765">Stir &amp;</tspan><tspan x="765" dy="4.5">enjoy</tspan></text>
      <text class="howto-caption" x="821" y="503"><tspan x="821">Add to</tspan><tspan x="821" dy="4.5">bottle</tspan></text>
      <text class="howto-caption" x="846" y="503"><tspan x="846">Shake</tspan><tspan x="846" dy="4.5">well</tspan></text>
      <text class="howto-caption" x="873" y="503"><tspan x="873">Enjoy</tspan><tspan x="873" dy="4.5">cold</tspan></text>

      <g class="general-facts">
        <text class="info-fact-title" x="802" y="525">TEA IN 3 SECONDS</text>
        <text class="info-fact" x="802" y="535">100% NATURAL, NO ADDITIVES, ARTIFICIAL FLAVORS</text>
        <text class="info-fact" x="802" y="542">OR PRESERVATIVES · 0 FAT / 0 SUGAR / 0 CALORIES</text>
        <text class="info-fact" x="802" y="549">IN CRYSTALS INSTEAD OF TEA POWDER OR TEA BAG</text>
        <text class="info-fact" x="802" y="556">SOLUBLE IN 3 SECONDS IN 200–300 ML HOT OR COLD WATER</text>
        <text class="info-fact" x="802" y="563">STIR OR SHAKE FOR BETTER DISSOLVING</text>
      </g>

      <text class="info-small info-center" x="802" y="582">DISTRIBUTED BY KORVENET AS®</text>
      <text class="info-small info-center" x="802" y="590">PO BOX: 4027</text>
      <text class="info-small info-center" x="802" y="598">OSLO, MØRKEDALSGATA 5, NORWAY</text>
      <text class="info-small info-center" x="802" y="606">LEARN MORE AT WWW.BRIMLEAF.EXAMPLE</text>
    </g>

    <!-- side panel B -->
    <g class="side-panel">
      <circle class="flavor-badge" cx="1046" cy="410" r="44"/>
      <text class="badge-arc" font-size="8.5"><textPath href="#arcSideB" startOffset="50%" text-anchor="middle">PREMIUM BLACK TEA</textPath></text>
      <text class="badge-name" x="1046" y="395" font-size="14">BRIM</text>
      <text class="badge-name" x="1046" y="413" font-size="14">INSTANT</text>
      <text class="badge-name" x="1046" y="431" font-size="14">LEMON</text>
      <text class="badge-count" x="1046" y="522" font-size="12">10 SACHETS</text>
      <text class="badge-count" x="1046" y="536" font-size="8">NETT 10x0.6 G</text>
      <circle class="brand-dot" cx="1046" cy="600" r="7"/>
      <text class="brand-name" x="1046" y="625" font-size="11.5" letter-spacing="1">BRIMLEAF</text>
    </g>
  </g>

  <!-- ===== Sachets ===== -->
  <g class="sachets">
    <g class="sachet">
      <rect class="foil" x="455" y="880" width="110" height="290"/>
      <rect x="459" y="894" width="102" height="256" fill="var(--leaf-mist)" role="img" aria-label="Watercolour tea leaf illustration on sachet"/>
      <rect x="459" y="894" width="102" height="256" fill="url(#leafWashA)"/>
      <circle class="flavor-badge" cx="510" cy="990" r="40"/>
      <text class="badge-arc" font-size="8"><textPath href="#arcSachetL" startOffset="50%" text-anchor="middle">PREMIUM BLACK TEA</textPath></text>
      <text class="badge-name" x="510" y="976" font-size="13">BRIM</text>
      <text class="badge-name" x="510" y="994" font-size="13">INSTANT</text>
      <text class="badge-name" x="510" y="1012" font-size="13">LEMON</text>
      <circle class="brand-dot" cx="510" cy="1075" r="8"/>
      <text class="brand-name" x="510" y="1102" font-size="13" letter-spacing="1">BRIMLEAF</text>
      <text class="sachet-weight" x="510" y="1142">0.6 G</text>
    </g>
    <g class="sachet">
      <rect class="foil" x="575" y="845" width="120" height="335"/>
      <rect x="579" y="860" width="112" height="300" fill="var(--leaf-mist)" role="img" aria-label="Watercolour tea leaf illustration on sachet"/>
      <rect x="579" y="860" width="112" height="300" fill="url(#leafWashA)"/>
      <circle class="flavor-badge" cx="635" cy="960" r="43"/>
      <text class="badge-arc" font-size="8.5"><textPath href="#arcSachetC" startOffset="50%" text-anchor="middle">PREMIUM BLACK TEA</textPath></text>
      <text class="badge-name" x="635" y="945" font-size="14">BRIM</text>
      <text class="badge-name" x="635" y="964" font-size="14">INSTANT</text>
      <text class="badge-name" x="635" y="983" font-size="14">LEMON</text>
      <circle class="brand-dot" cx="635" cy="1065" r="9"/>
      <text class="brand-name" x="635" y="1095" font-size="14" letter-spacing="1">BRIMLEAF</text>
      <text class="sachet-weight" x="635" y="1140">0.6 G</text>
    </g>
    <g class="sachet">
      <rect class="foil" x="705" y="880" width="110" height="290"/>
      <rect x="709" y="894" width="102" height="256" fill="var(--leaf-mist)" role="img" aria-label="Watercolour tea leaf illustration on sachet"/>
      <rect x="709" y="894" width="102" height="256" fill="url(#leafWashA)"/>
      <circle class="flavor-badge" cx="760" cy="990" r="40"/>
      <text class="badge-arc" font-size="8"><textPath href="#arcSachetR" startOffset="50%" text-anchor="middle">PREMIUM BLACK TEA</textPath></text>
      <text class="badge-name" x="760" y="976" font-size="13">BRIM</text>
      <text class="badge-name" x="760" y="994" font-size="13">INSTANT</text>
      <text class="badge-name" x="760" y="1012" font-size="13">LEMON</text>
      <circle class="brand-dot" cx="760" cy="1075" r="8"/>
      <text class="brand-name" x="760" y="1102" font-size="13" letter-spacing="1">BRIMLEAF</text>
      <text class="sachet-weight" x="760" y="1142">0.6 G</text>
    </g>
  </g>
</svg>
</body>
</html>
```